Report Design Template Needed for Strategy Consulting Co.

I have a small consulting business that does market research, develops marketing strategy, and does business development work (sales, finding partners, preparing for investors) for small and medium-sized companies who can’t afford their own full-time marketing person.

Most of my reports are PowerPoint Decks. There is usually a Title Page, a Table of Contents, an Executive Summary, a Detailed Findings section (with some section breaks, so I need a divider page between sections), and a Recommendations section.

I need a report template/style that is attractive, professional and not too bold such that it takes away from the content, which is what they are paying for.

I have color palette ideas and graphics in the attached brief. Please let me know if you need anything else, or if you need graphic files.

Thank you!!

Target Market(s)

Small business professionals, scientists, business development executives.

Industry/Entity Type

Marketing

Font styles to use
Sans Serif

Requirements
Must have
• Should have the sections listed in the brief. Also, need to be able to import the template complete.
Should not have
• Background must not overtake the text

```html
<!DOCTYPE html>
<html lang="en">
<head>
<meta charset="utf-8">
<title>Report Template – Two Column Content Page</title>
<link rel="stylesheet" href="https://fonts.googleapis.com/css2?family=Oxanium:wght@500;700&family=Exo+2:wght@500&family=Open+Sans:wght@400&display=swap">
<style>
  :root {
    --navy: #1d5470;
    --navy-text: #1e5673;
    --accent-green: #8fa93a;
    --body-text: #3f3f3f;
    --page-white: #ffffff;
    --page-tint: #e6eff7;
    --frame-grey: #dfe3e6;
  }
  * { margin: 0; padding: 0; box-sizing: border-box; }
  html, body { width: 1200px; height: 900px; overflow: hidden; background: var(--page-white); }
  .slide {
    position: relative;
    width: 1200px;
    height: 900px;
    overflow: hidden;
    background:
      radial-gradient(ellipse 60% 45% at 55% 50%, var(--page-tint) 0%, rgba(230,239,247,0) 70%),
      linear-gradient(180deg, #f3f7fb 0%, #ffffff 45%, #f1f5fa 100%);
  }
  .slide-header {
    position: absolute;
    top: 0; left: 0;
    width: 100%;
    height: 86px;
    background: var(--navy);
    border-bottom: 7px solid var(--accent-green);
    height: 93px;
  }
  .project-title {
    position: absolute;
    left: 22px;
    top: 16px;
    font-family: 'Oxanium', sans-serif;
    font-weight: 700;
    font-size: 46px;
    letter-spacing: 2px;
    color: var(--page-white);
    text-transform: uppercase;
    line-height: 1;
  }
  .content-column {
    position: absolute;
    top: 172px;
    width: 520px;
  }
  .content-column.left { left: 36px; }
  .content-column.right { left: 638px; }
  .column-heading {
    font-family: 'Exo 2', sans-serif;
    font-weight: 500;
    font-size: 33px;
    color: var(--navy-text);
    line-height: 1;
    white-space: nowrap;
  }
  .feature-photo {
    margin-top: 43px;
    width: 518px;
    height: 181px;
    border: 3px solid var(--page-white);
    box-shadow: 0 0 0 1px var(--frame-grey);
    background: linear-gradient(180deg, #a9c3dc 0%, #c9d6df 35%, #a8775c 70%, #7d5444 100%);
  }
  .body-copy {
    font-family: 'Open Sans', sans-serif;
    font-size: 19px;
    line-height: 33px;
    color: var(--body-text);
    margin-top: 16px;
  }
  .body-copy + .body-copy { margin-top: 33px; }
  .body-copy span { display: block; white-space: nowrap; }
  .slide-footer {
    position: absolute;
    left: 0;
    top: 801px;
    width: 100%;
    height: 99px;
    border-top: 2px solid var(--accent-green);
    background: linear-gradient(180deg, #eef2f5 0%, #ffffff 30%);
  }
  .copyright {
    position: absolute;
    left: 22px;
    top: 48px;
    font-family: 'Oxanium', sans-serif;
    font-weight: 500;
    font-size: 17px;
    letter-spacing: 0.5px;
    color: var(--navy-text);
    text-transform: uppercase;
  }
  .brand-name {
    position: absolute;
    right: 20px;
    top: 30px;
    font-family: 'Exo 2', sans-serif;
    font-weight: 500;
    font-size: 40px;
    color: var(--navy-text);
    line-height: 1;
    display: flex;
    align-items: center;
    gap: 12px;
  }
  .brand-mark {
    width: 14px;
    height: 14px;
    border-radius: 50%;
    background: var(--navy-text);
  }
</style>
</head>
<body>
<main class="slide">
  <header class="slide-header">
    <h1 class="project-title">Project Title Here</h1>
  </header>

  <section class="content-column left">
    <h2 class="column-heading">Lorem ipsum dolor sit ipsum</h2>
    <div class="feature-photo" role="img" aria-label="Photo of a smiling homeowner standing in front of a brick house"></div>
    <p class="body-copy">
      <span>Lorem ipsum dolor sit ipsum Lorem ipsum dolor sit ipsum</span>
      <span>Lorem ipsum dolor sit ipsum Lorem ipsum dolor sit ipsum</span>
      <span>lorem ipsum dolor sit ipsum Lorem ipsum dolor sit ipsum</span>
      <span>Lorem ipsum dolor sit ipsum</span>
    </p>
    <p class="body-copy">
      <span>Lorem ipsum dolor sit ipsum Lorem ipsum dolor sit ipsum</span>
      <span>Lorem ipsum dolor sit ipsum Lorem ipsum dolor sit ipsum</span>
      <span>lorem ipsum dolor sit ipsum Lorem ipsum dolor sit ipsum</span>
      <span>Lorem ipsum dolor sit ipsum</span>
    </p>
  </section>

  <section class="content-column right">
    <h2 class="column-heading">Lorem ipsum dolor sit ipsum</h2>
    <div class="feature-photo" role="img" aria-label="Photo of a smiling homeowner standing in front of a brick house"></div>
    <p class="body-copy">
      <span>Lorem ipsum dolor sit ipsum Lorem ipsum dolor sit ipsum</span>
      <span>Lorem ipsum dolor sit ipsum Lorem ipsum dolor sit ipsum</span>
      <span>lorem ipsum dolor sit ipsum Lorem ipsum dolor sit ipsum</span>
      <span>Lorem ipsum dolor sit ipsum</span>
    </p>
    <p class="body-copy">
      <span>Lorem ipsum dolor sit ipsum Lorem ipsum dolor sit ipsum</span>
      <span>Lorem ipsum dolor sit ipsum Lorem ipsum dolor sit ipsum</span>
      <span>lorem ipsum dolor sit ipsum Lorem ipsum dolor sit ipsum</span>
      <span>Lorem ipsum dolor sit ipsum</span>
    </p>
  </section>

  <footer class="slide-footer">
    <p class="copyright">Copyright text here</p>
    <div class="brand-name"><span class="brand-mark"></span>Horizon Partners</div>
  </footer>
</main>
</body>
</html>
```